Legal Journal cover - modern and sylish

We require a cover design for a new, modern and digital legal academic journal. Attached is our logo so you can get an idea of the feel. This academic journal will have several editions per year.Requirements for the cover design:-The feel of the cover is to be modern -In harmony with our logo-While staying uniform and set in its design,

Colors
ec1f27

Requirements
Must have
• 1) Colour. Each edition will use different colours. (So we will need the source files to be able to continue to do this)
• 2) An image section. We would like to be able to put in different image or photo with each edition. So we need to have a section, most likely in the shape of a strip, that can include a different image or photo each edition. This part is where we can put a different image in for each edition. So this section would need to be able to accommodate different types of images. It could be a single square. Or it could be a line (a strip) that an image or images.
• 3) A title for the edition and volume and number. Like this:
• Volume 34, No 2 (2016): Contemporary Issues in Criminal Law
• I have attached a range of journals I found online to serve as inspiration.

```html
<!DOCTYPE html>
<html lang="en">
<head>
<meta charset="utf-8">
<title>Legal Lens Legal Journal – Edition Covers 2019</title>
<link href="https://fonts.googleapis.com/css2?family=Crimson+Text:wght@400;600;700&display=swap" rel="stylesheet">
<style>
  :root {
    --brand-red: #e3231f;
    --neutral-grey: #71706e;
    --shadow-grey: #9d9d9c;
    --paper: #ffffff;
    --title-grey: #6f6f6e;
    --edition-september: #e3231f;
    --edition-october: #0380b5;
    --edition-november: #e0a304;
    --edition-december: #6b9d2f;
  }
  html, body {
    margin: 0;
    padding: 0;
    overflow: hidden;
  }
  body {
    width: 848px;
    height: 1200px;
    background: var(--paper);
    position: relative;
    font-family: "Crimson Text", serif;
  }
  .cover {
    position: absolute;
    width: 330.7px;
    height: 465.5px;
  }
  .cover svg { display: block; width: 100%; height: 100%; }
  .cover--september { left: 50.2px;  top: 94.9px;  --accent: var(--edition-september); }
  .cover--october   { left: 455.8px; top: 94.9px;  --accent: var(--edition-october); }
  .cover--november  { left: 50.2px;  top: 621.4px; --accent: var(--edition-november); }
  .cover--december  { left: 455.8px; top: 621.4px; --accent: var(--edition-december); }

  .accent-block { fill: var(--accent); }
  .neutral-block { fill: var(--neutral-grey); }
  .paper-disc { fill: var(--paper); }
  .brand-band { fill: var(--brand-red); }
  .page-shadow { fill: var(--shadow-grey); }
  .ring-outer { fill: var(--brand-red); }
  .ring-inner { fill: var(--neutral-grey); }
  .brand-dot { fill: var(--brand-red); }
  .brand-name {
    fill: var(--brand-red);
    font-family: "Crimson Text", serif;
    font-weight: 600;
    font-size: 30px;
  }
  .journal-title {
    fill: var(--title-grey);
    font-family: "Crimson Text", serif;
    font-weight: 600;
    font-size: 33px;
  }
  .edition-date {
    fill: var(--paper);
    font-family: "Crimson Text", serif;
    font-weight: 700;
    font-size: 22px;
  }
</style>
</head>
<body>

<!-- September edition -->
<div class="cover cover--september">
  <svg viewBox="0 0 645 908" aria-label="Legal Lens Legal Journal, September 2019 cover">
    <defs>
      <linearGradient id="photo-september" x1="0" y1="0" x2="1" y2="1">
        <stop offset="0" stop-color="#e8ecec"/>
        <stop offset="0.5" stop-color="#c9a68a"/>
        <stop offset="1" stop-color="#d9433a"/>
      </linearGradient>
    </defs>
    <rect class="page-shadow" x="636" y="8" width="9" height="900"/>
    <rect class="page-shadow" x="8" y="899" width="637" height="9"/>
    <rect class="accent-block" x="0" y="0" width="219" height="400"/>
    <rect class="neutral-block" x="0" y="422" width="208" height="435"/>
    <rect class="accent-block" x="230" y="422" width="406" height="435"/>
    <circle class="paper-disc" cx="219" cy="305" r="194"/>
    <rect class="brand-band" x="219" y="210" width="417" height="19"/>
    <rect class="brand-band" x="219" y="379" width="417" height="20"/>
    <circle class="ring-outer" cx="219" cy="305" r="171"/>
    <circle class="ring-inner" cx="219" cy="305" r="150"/>
    <circle cx="219" cy="305" r="126" fill="url(#photo-september)" role="img" aria-label="Edition photo: two students working together at a laptop"/>
    <circle class="brand-dot" cx="404" cy="80" r="10"/>
    <text class="brand-name" x="422" y="90" textLength="178" lengthAdjust="spacingAndGlyphs">LEGAL LENS</text>
    <text class="journal-title" x="406" y="297">Legal Lens</text>
    <text class="journal-title" x="406" y="335">Legal Journal</text>
    <text class="edition-date" x="514" y="830" text-anchor="middle">September 2019</text>
    <rect class="brand-band" x="0" y="878" width="636" height="20"/>
  </svg>
</div>

<!-- October edition -->
<div class="cover cover--october">
  <svg viewBox="0 0 645 908" aria-label="Legal Lens Legal Journal, October 2019 cover">
    <defs>
      <linearGradient id="photo-october" x1="0" y1="0" x2="1" y2="1">
        <stop offset="0" stop-color="#dfe5ea"/>
        <stop offset="0.5" stop-color="#a8a39c"/>
        <stop offset="1" stop-color="#5b5552"/>
      </linearGradient>
    </defs>
    <rect class="page-shadow" x="636" y="8" width="9" height="900"/>
    <rect class="page-shadow" x="8" y="899" width="637" height="9"/>
    <rect class="accent-block" x="0" y="0" width="219" height="400"/>
    <rect class="neutral-block" x="0" y="422" width="208" height="435"/>
    <rect class="accent-block" x="230" y="422" width="406" height="435"/>
    <circle class="paper-disc" cx="219" cy="305" r="194"/>
    <rect class="brand-band" x="219" y="210" width="417" height="19"/>
    <rect class="brand-band" x="219" y="379" width="417" height="20"/>
    <circle class="ring-outer" cx="219" cy="305" r="171"/>
    <circle class="ring-inner" cx="219" cy="305" r="150"/>
    <circle cx="219" cy="305" r="126" fill="url(#photo-october)" role="img" aria-label="Edition photo: a group of business professionals"/>
    <circle class="brand-dot" cx="404" cy="80" r="10"/>
    <text class="brand-name" x="422" y="90" textLength="178" lengthAdjust="spacingAndGlyphs">LEGAL LENS</text>
    <text class="journal-title" x="406" y="297">Legal Lens</text>
    <text class="journal-title" x="406" y="335">Legal Journal</text>
    <text class="edition-date" x="504" y="830" text-anchor="middle">October 2019</text>
    <rect class="brand-band" x="0" y="878" width="636" height="20"/>
  </svg>
</div>

<!-- November edition -->
<div class="cover cover--november">
  <svg viewBox="0 0 645 908" aria-label="Legal Lens Legal Journal, November 2019 cover">
    <defs>
      <linearGradient id="photo-november" x1="0" y1="0" x2="1" y2="1">
        <stop offset="0" stop-color="#d9d2c6"/>
        <stop offset="0.5" stop-color="#a7654a"/>
        <stop offset="1" stop-color="#e6b931"/>
      </linearGradient>
    </defs>
    <rect class="page-shadow" x="636" y="8" width="9" height="900"/>
    <rect class="page-shadow" x="8" y="899" width="637" height="9"/>
    <rect class="accent-block" x="0" y="0" width="219" height="400"/>
    <rect class="neutral-block" x="0" y="422" width="208" height="435"/>
    <rect class="accent-block" x="230" y="422" width="406" height="435"/>
    <circle class="paper-disc" cx="219" cy="305" r="194"/>
    <rect class="brand-band" x="219" y="210" width="417" height="19"/>
    <rect class="brand-band" x="219" y="379" width="417" height="20"/>
    <circle class="ring-outer" cx="219" cy="305" r="171"/>
    <circle class="ring-inner" cx="219" cy="305" r="150"/>
    <circle cx="219" cy="305" r="126" fill="url(#photo-november)" role="img" aria-label="Edition photo: two smiling students sharing a yellow book"/>
    <circle class="brand-dot" cx="404" cy="80" r="10"/>
    <text class="brand-name" x="422" y="90" textLength="178" lengthAdjust="spacingAndGlyphs">LEGAL LENS</text>
    <text class="journal-title" x="406" y="297">Legal Lens</text>
    <text class="journal-title" x="406" y="335">Legal Journal</text>
    <text class="edition-date" x="514" y="830" text-anchor="middle">November 2019</text>
    <rect class="brand-band" x="0" y="878" width="636" height="20"/>
  </svg>
</div>

<!-- December edition -->
<div class="cover cover--december">
  <svg viewBox="0 0 645 908" aria-label="Legal Lens Legal Journal, December 2019 cover">
    <defs>
      <linearGradient id="photo-december" x1="0" y1="0" x2="1" y2="1">
        <stop offset="0" stop-color="#8fb45a"/>
        <stop offset="0.5" stop-color="#c7c3bc"/>
        <stop offset="1" stop-color="#4f8a2c"/>
      </linearGradient>
    </defs>
    <rect class="page-shadow" x="636" y="8" width="9" height="900"/>
    <rect class="page-shadow" x="8" y="899" width="637" height="9"/>
    <rect class="accent-block" x="0" y="0" width="219" height="400"/>
    <rect class="neutral-block" x="0" y="422" width="208" height="435"/>
    <rect class="accent-block" x="230" y="422" width="406" height="435"/>
    <circle class="paper-disc" cx="219" cy="305" r="194"/>
    <rect class="brand-band" x="219" y="210" width="417" height="19"/>
    <rect class="brand-band" x="219" y="379" width="417" height="20"/>
    <circle class="ring-outer" cx="219" cy="305" r="171"/>
    <circle class="ring-inner" cx="219" cy="305" r="150"/>
    <circle cx="219" cy="305" r="126" fill="url(#photo-december)" role="img" aria-label="Edition photo: students reading on the grass"/>
    <circle class="brand-dot" cx="404" cy="80" r="10"/>
    <text class="brand-name" x="422" y="90" textLength="178" lengthAdjust="spacingAndGlyphs">LEGAL LENS</text>
    <text class="journal-title" x="406" y="297">Legal Lens</text>
    <text class="journal-title" x="406" y="335">Legal Journal</text>
    <text class="edition-date" x="513" y="830" text-anchor="middle">December 2019</text>
    <rect class="brand-band" x="0" y="878" width="636" height="20"/>
  </svg>
</div>

</body>
</html>
```